Business and Success Coaching Business Card

Need a business card for my coaching business. I coach small businesses, career professionals and, individuals wanting to unlock their human potential and achieve excellence. At the heart of our methodology is the Building Lasting Outcomes On Momentum (BLOOM) approach to formulate empowerment, create principles for success and setting achievable outcomes. I would like something that incorporates our new logo, something clean and sharp with a solid darker, but complementary background, color on the card front. The back should be white where there will be room for three questions

Target Market(s)

People looking to advance and improve themselves through a success coach

Industry/Entity Type

Life Coaching

Contact Information for Business Card

Contact information on card.
Business name on front of card
Questions on back

Font styles to use
Other font styles liked:
• Century Gothic or other Serif style fonts that look similar to Century Gothic

Colors

Designer to choose colors to be used in the design.

Requirements
Must have
• Logo on front of card
• Business name - The Bright Stride
• Contact name - Ray Dalton
• Address - Box 5196, Maple Hill, OR 80174-5196
• Phone number - 303-555-0148
• Email address - dalton.ray@thebrightstride.com
• Certifications - CBC, CHt, PCT, MNLP
• Back of card
• Three questions on the back of the card:
• If you were at your best, what would you do right now?
• What is the decision you have been avoiding?
• What's one action you could take in the next 10 minutes?
Nice to have
• I would like to see a solid color on the front of the card that compliments the logo.
• Back should be white, or could be contrasting, but need to have the three questions.

```html
<!DOCTYPE html>
<html lang="en">
<head>
<meta charset="utf-8">
<title>The Bright Stride – Business Card</title>
<link href="https://fonts.googleapis.com/css2?family=Montserrat:wght@400;500;600;700&display=swap" rel="stylesheet">
<style>
  :root {
    --page: #ecebe8;
    --card: #333437;
    --card-edge: #1e88e5;
    --accent: #2f8fe6;
    --text: #f2f2f2;
    --muted: #d6d6d6;
    --ghost: #3b3c40;
    --rule: #c9c9c9;
  }
  * { box-sizing: border-box; margin: 0; padding: 0; }
  html, body {
    width: 1200px; height: 800px; overflow: hidden;
    background: var(--page);
    font-family: "Montserrat", sans-serif;
  }
  .canvas {
    position: relative; width: 1200px; height: 800px;
    display: flex; align-items: center; justify-content: center; gap: 40px;
  }
  .card {
    position: relative; width: 530px; height: 303px;
    background: var(--card);
    border-left: 3px solid var(--card-edge);
    border-bottom: 3px solid var(--card-edge);
    overflow: hidden;
  }

  /* Back: questions */
  .card-back .brand-ghost {
    position: absolute; top: 72px; left: 0; right: 0;
    text-align: center;
    font-size: 34px; font-weight: 700; color: var(--ghost);
  }
  .questions {
    position: absolute; left: 0; right: 0; bottom: 40px;
    list-style: none; text-align: center;
    font-size: 15.5px; font-weight: 500; line-height: 1.45;
  }
  .questions .q-accent { color: var(--accent); }
  .questions .q-light { color: var(--text); }

  /* Front: identity and contact */
  .card-front { display: flex; align-items: center; }
  .brand {
    width: 250px; padding-left: 28px; color: var(--text);
  }
  .brand-name { font-size: 22px; font-weight: 700; letter-spacing: -0.2px; white-space: nowrap; }
  .brand-tagline { font-size: 11.5px; font-weight: 500; margin-top: 3px; color: var(--muted); white-space: nowrap; }
  .divider {
    width: 1px; height: 122px; background: var(--rule); margin-right: 16px;
  }
  .contact { color: var(--text); font-size: 12.5px; line-height: 1.5; white-space: nowrap; }
  .contact-name {
    font-size: 17px; font-weight: 700; color: var(--accent);
    text-transform: uppercase; letter-spacing: 0.3px; line-height: 1.3;
  }
  .contact-line { display: flex; align-items: center; gap: 6px; }
  .contact-line svg { width: 11px; height: 11px; fill: var(--accent); flex: none; }
</style>
</head>
<body>
<main class="canvas">
  <section class="card card-back" aria-label="Card back">
    <div class="brand-ghost">The Bright Stride</div>
    <ul class="questions">
      <li class="q-accent">If you were at your best, what would you do right now?</li>
      <li class="q-light">What is the decision you have been avoiding?</li>
      <li class="q-accent">What's one action you could take in the next 10 minutes?</li>
    </ul>
  </section>

  <section class="card card-front" aria-label="Card front">
    <div class="brand">
      <div class="brand-name">The Bright Stride</div>
      <div class="brand-tagline">Step into your next season</div>
    </div>
    <div class="divider"></div>
    <div class="contact">
      <div class="contact-name">Ray Dalton</div>
      <div class="credentials">CBC, CHt, PCT, MNLP</div>
      <div>Box 5196</div>
      <div>Maple Hill, OR 80174-5196</div>
      <div class="contact-line">
        <svg viewBox="0 0 24 24" aria-hidden="true"><path d="M6.6 10.8a15.1 15.1 0 0 0 6.6 6.6l2.2-2.2a1 1 0 0 1 1-.25 11.4 11.4 0 0 0 3.6.57 1 1 0 0 1 1 1V20a1 1 0 0 1-1 1A17 17 0 0 1 3 4a1 1 0 0 1 1-1h3.5a1 1 0 0 1 1 1c0 1.250.2 2.450.57 3.570a1 1 0 0 1-.25 1z"/></svg>
        <span>303-555-0148</span>
      </div>
      <div class="contact-line">
        <svg viewBox="0 0 24 24" aria-hidden="true"><path d="M2 5h20v14H2z M3.5 6.5v.4L12 12.5l8.5-5.6v-.4z" fill-rule="evenodd"/></svg>
        <span>dalton.ray@thebrightstride.com</span>
      </div>
    </div>
  </section>
</main>
</body>
</html>
```